Seeds of Renewal needs a business card design

I need a business card design for my company to promote my new Christian non-fiction book, "Where the Quiet River Bends." I also want it to promote my web site, www.seedsofrenewalway.com. The book is about empowering people to be transformed through a deeper relationship with God. I am picturing a design with a dove over water that matches the colors of my book cover, blue, white, yellow, and orange. Fire and light would also be possible elements of the design. I would like to be able to use the dove by itself as a logo for my business. This is my first book and I do not know if others will follow. The name of my publishing company is Lantern Valley Press, named after Gideon in the Bible story from the book of Judges. My book was independently published and was recently selected as a finalist for the 2015 Bright Horizon SMALLPRESS book prize in the Christian non-fiction genre.

Target Market(s)

People who are hungry for more of God and who want to experience deep change in their lives.

Industry/Entity Type

Business

Contact Information for Business Card

Dana Whitfield
Author
Where the Quiet River Bends
4283 Maple Hollow Lane
Austin, Texas 78952-1184
512-555-0147 512-555-0193
dana-whitfield@brightmailbox.net
www.seedsofrenewalway.com

Colors
0355a3
3377b5
85acd3
cedeed
fbee3e
ffc214

Requirements
Must have
• A dove with a blue background, peaceful and appealing
Nice to have
• Water and fire or light
Should not have
• Violence or fear-producing images

```html
<!DOCTYPE html>
<html lang="en">
<head>
<meta charset="utf-8">
<title>Seeds of Renewal – Business Card</title>
<link rel="stylesheet" href="https://fonts.googleapis.com/css2?family=Arimo:wght@400;700&family=Cinzel:wght@400&family=Great+Vibes&family=Cormorant+Garamond:wght@500&display=swap">
<style>
  :root {
    --page: #e6e6e4;
    --blue-deep: #0355a3;
    --blue-mid: #3377b5;
    --blue-light: #85acd3;
    --blue-pale: #cedeed;
    --navy: #0a1f6b;
    --gold: #ffc214;
    --yellow: #fbee3e;
    --white: #ffffff;
  }
  * { margin: 0; padding: 0; box-sizing: border-box; }
  html, body {
    width: 1200px; height: 1200px; overflow: hidden;
    background: var(--page);
  }
  .sheet {
    position: relative; width: 1200px; height: 1200px;
    display: flex; flex-direction: column; align-items: center; justify-content: center; gap: 60px;
  }
  .card {
    position: relative; width: 840px; height: 480px; overflow: hidden;
    box-shadow: 0 6px 18px rgba(0,0,0,.18);
  }

  /* Front: book cover, turned sideways */
  .card--front { background: var(--navy); }
  .cover {
    position: absolute; width: 480px; height: 840px;
    left: 180px; top: -180px;
    transform: rotate(-90deg);
  }
  .cover__art {
    position: absolute; inset: 0;
    background:
      radial-gradient(ellipse at 30% 45%, rgba(133,172,211,.55), transparent 55%),
      radial-gradient(ellipse at 70% 20%, rgba(51,119,181,.6), transparent 60%),
      linear-gradient(180deg, #123a9c 0%, #1d4fb8 45%, #0f2f8a 100%);
  }
  .cover__band {
    position: absolute; left: 0; right: 0; top: 615px; height: 175px;
    background: linear-gradient(180deg, rgba(51,119,181,.55), rgba(3,85,163,.75));
  }
  .cover__title {
    position: absolute; left: 0; right: 0; top: 34px;
    text-align: center;
    font-family: "Cinzel", serif; color: var(--white);
    font-size: 76px; line-height: 1.02; letter-spacing: 2px;
  }
  .cover__script {
    position: absolute; left: 0; right: 0; top: 370px; text-align: center;
    font-family: "Great Vibes", cursive; color: var(--gold);
    font-size: 110px; line-height: 1;
  }
  .cover__subtitle {
    position: absolute; left: 0; right: 0; top: 530px; text-align: center;
    font-family: "Cormorant Garamond", serif; color: var(--white);
    font-size: 19px; letter-spacing: 1px; line-height: 1.25; text-transform: uppercase;
  }
  .cover__author {
    position: absolute; left: 0; right: 0; top: 682px; text-align: center;
    font-family: "Cormorant Garamond", serif; color: var(--gold);
    font-size: 32px; letter-spacing: 1px; text-transform: uppercase;
  }

  /* Back: contact side */
  .card--back {
    background: radial-gradient(ellipse at 35% 70%, #0b66a8 0%, var(--blue-deep) 55%, #0a50a6 100%);
    font-family: "Arimo", sans-serif; color: var(--white);
  }
  .brand {
    position: absolute; left: 78px; top: 76px;
    display: flex; align-items: center; gap: 14px;
  }
  .brand__dot { width: 36px; height: 36px; border-radius: 50%; background: var(--blue-pale); }
  .brand__name { font-size: 24px; font-weight: 400; color: var(--white); }
  .holder { position: absolute; right: 96px; top: 130px; text-align: right; }
  .holder__name { font-size: 31px; }
  .holder__name b { font-weight: 700; }
  .holder__role { font-size: 25px; margin-top: 2px; }
  .contact { position: absolute; left: 300px; top: 228px; font-size: 21px; line-height: 1.2; }
  .contact__row { display: flex; align-items: flex-start; gap: 14px; margin-bottom: 14px; }
  .contact__item { display: flex; align-items: center; gap: 14px; }
  .contact__item--mobile { margin-left: 18px; }
  .icon { width: 20px; height: 20px; flex: none; fill: var(--white); margin-top: 1px; }
</style>
</head>
<body>
<main class="sheet">

  <section class="card card--front" aria-label="Book cover side">
    <div class="cover">
      <div class="cover__art" role="img" aria-label="Deep blue watercolour background with soft sparkles of light on water"></div>
      <div class="cover__band"></div>
      <h1 class="cover__title">WHERE<br>THE<br>QUIET<br>RIVER</h1>
      <div class="cover__script">Bends</div>
      <p class="cover__subtitle">Growing into the life<br>you were made to live</p>
      <p class="cover__author">Dana Whitfield</p>
    </div>
  </section>

  <section class="card card--back" aria-label="Contact side">
    <div class="brand">
      <span class="brand__dot"></span>
      <span class="brand__name">Seeds of Renewal</span>
    </div>

    <div class="holder">
      <div class="holder__name"><b>Dana</b> Whitfield</div>
      <div class="holder__role">(Author)</div>
    </div>

    <div class="contact">
      <div class="contact__row">
        <svg class="icon" viewBox="0 0 24 24"><path d="M12 2a7 7 0 0 0-7 7c0 5 7 13 7 13s7-8 7-13a7 7 0 0 0-7-7zm0 9.5A2.5 2.5 0 1 1 12 6.5a2.5 2.5 0 0 1 0 5z"/></svg>
        <span>4283 Maple Hollow Lane Austin,<br>Texas - 78952</span>
      </div>
      <div class="contact__row">
        <span class="contact__item">
          <svg class="icon" viewBox="0 0 24 24"><path d="M4 9c0-3 4-5 8-5s8 2 8 5l-3 2-2-2.5H9L7 11 4 9zm3 3h10l2 8H5l2-8zm5 2a2 2 0 1 0 0 4 2 2 0 0 0 0-4z"/></svg>
          512-555-0147
        </span>
        <span class="contact__item contact__item--mobile">
          <svg class="icon" viewBox="0 0 24 24"><path d="M7 2h10a1 1 0 0 1 1 1v18a1 1 0 0 1-1 1H7a1 1 0 0 1-1-1V3a1 1 0 0 1 1-1zm1 3v13h8V5H8zm4 14.2a.9.9 0 1 0 0 1.8.9.9 0 0 0 0-1.8z"/></svg>
          512-555-0193
        </span>
      </div>
      <div class="contact__row">
        <svg class="icon" viewBox="0 0 24 24"><path d="M3 5h18v14H3V5zm2 2v.4l7 5 7-5V7H5zm14 2.9-7 5-7-5V17h14V9.9z"/></svg>
        <span>dana-whitfield@brightmailbox.net</span>
      </div>
      <div class="contact__row">
        <svg class="icon" viewBox="0 0 24 24"><path d="M12 2a10 10 0 1 0 0 20 10 10 0 0 0 0-20zm6.9 9h-3a15 15 0 0 0-1.3-5.6A8 8 0 0 1 18.9 11zM12 4.1c.9 1.2 1.8 3.6 1.9 6.9h-3.8c.1-3.3 1-5.7 1.9-6.9zM9.4 5.4A15 15 0 0 0 8.1 11h-3a8 8 0 0 1 4.3-5.6zM5.1 13h3a15 15 0 0 0 1.3 5.6A8 8 0 0 1 5.1 13zm6.9 6.9c-.9-1.2-1.8-3.6-1.9-6.9h3.8c-.1 3.3-1 5.7-1.9 6.9zm2.6-1.3a15 15 0 0 0 1.3-5.6h3a8 8 0 0 1-4.3 5.6z"/></svg>
        <span>www.seedsofrenewalway.com</span>
      </div>
    </div>
  </section>

</main>
</body>
</html>
```